Webdesign für Onlineshop für hochwertige Porzellan- und Glaswaren
Zielgruppe
Es soll einer neuer Onlineshop für hochwertige Porzellan- und Glaswaren entstehen.
Aufgabenstellung
Logo ist bereits vorhanden. Es soll ein hochwertiges und dennoch übersichtliches Design erstellt werden.
Anbei einige Referenzen:
https://www.velumora.com/
https://www.kandrivel.de/en-de/
https://pemoxa.it/en/home-page/

```html
<!DOCTYPE html>
<html lang="de">
<head>
<meta charset="utf-8">
<title>Merante – Produkte</title>
<link href="https://fonts.googleapis.com/css2?family=Playfair+Display:wght@600;700&family=Lato:ital,wght@0,400;0,700;1,400&display=swap" rel="stylesheet">
<style>
:root{
  --navy:#2b2d6e;
  --navy-text:#2d2f72;
  --ink:#333;
  --soft-blue:#a9c7f6;
  --header-bg:#f0eeeb;
  --grid-bg:#eeece9;
  --white:#fff;
  --muted:#555;
}
*{box-sizing:border-box;margin:0;padding:0}
html,body{width:1200px;height:3502px;overflow:hidden;background:var(--white)}
.page{width:390px;height:1138px;transform:scale(3.07693);transform-origin:0 0;position:relative;overflow:hidden;font-family:'Lato',sans-serif;color:var(--ink)}
.site-header{position:absolute;left:0;top:0;width:390px;height:110px;background:var(--header-bg)}
.menu-icon{position:absolute;left:16px;top:22px}
.brand{position:absolute;left:0;right:0;top:22px;text-align:center;font-family:'Playfair Display',serif;font-weight:600;font-size:15px;letter-spacing:1.5px;color:var(--navy)}
.header-icons{position:absolute;right:16px;top:22px;display:flex;gap:9px}
.search{position:absolute;left:16px;top:55px;width:356px;height:40px;border:1px solid #444;border-radius:20px;background:var(--white)}
.search span{position:absolute;left:17px;top:11px;font-style:italic;font-size:13px;color:#888}
.search svg{position:absolute;right:14px;top:11px}
.hero{position:absolute;left:0;top:110px;width:390px;height:190px;background:radial-gradient(ellipse at 75% 75%,#6a6a6a 0%,#3a3a3a 35%,#141414 75%),#111}
.hero h1{position:absolute;left:0;right:0;top:46px;text-align:center;font-family:'Playfair Display',serif;font-weight:700;font-size:26px;color:var(--white)}
.category-tabs{position:absolute;left:26px;top:105px;display:flex;gap:6px}
.tab{width:110px;height:30px;border:1.5px solid var(--soft-blue);border-radius:15px;color:var(--white);font-size:13px;font-weight:700;display:flex;align-items:center;justify-content:center;background:rgba(0,0,0,.25)}
.tab.is-active{background:var(--soft-blue);color:var(--white)}
.toolbar{position:absolute;left:0;top:300px;width:390px;height:52px;background:var(--white)}
.filter{position:absolute;left:28px;top:17px;display:flex;align-items:center;gap:7px;font-size:15px;font-weight:700;color:var(--navy-text)}
.sort{position:absolute;left:244px;top:11px;width:135px;height:33px;border:1px solid var(--navy);border-radius:3px;font-size:13px;color:var(--navy-text);padding:8px 0 0 15px}
.sort svg{position:absolute;right:10px;top:12px}
.product-grid{position:absolute;left:0;top:352px;width:390px;height:800px;background:var(--grid-bg);display:grid;grid-template-columns:192px 190px;column-gap:8px;row-gap:9px;padding-top:10px}
.card{height:272px;background:var(--white);position:relative;text-align:center}
.card .fav{position:absolute;right:16px;top:11px}
.plate{position:absolute;left:50%;top:22px;width:102px;height:102px;margin-left:-51px;border-radius:50%;background:radial-gradient(circle,#cdc9c2 0%,#a9aea8 30%,#8a908c 42%,#c6b49e 60%,#d8c3a4 85%,#cbb496 100%);box-shadow:0 2px 3px rgba(0,0,0,.15)}
.card h2{position:absolute;left:0;right:0;top:160px;font-family:'Playfair Display',serif;font-weight:700;font-size:12.5px;color:#333}
.card .desc{position:absolute;left:0;right:0;top:180px;font-size:8.5px;color:var(--muted)}
.card .price{position:absolute;left:0;right:0;top:194px;font-family:'Playfair Display',serif;font-weight:700;font-size:12px;color:var(--navy-text)}
.cart-btn{position:absolute;left:23px;top:226px;width:145px;height:31px;border-radius:4px;background:var(--soft-blue);display:flex;align-items:center;justify-content:center}
.card:nth-child(even) .cart-btn{left:22px}
.cart-btn.is-hover{background:var(--navy)}
</style>
</head>
<body>
<div class="page">
  <header class="site-header">
    <svg class="menu-icon" width="24" height="18" viewBox="0 0 24 18"><path d="M0 1h24M0 9h24M0 17h24" stroke="#555" stroke-width="1.5"/></svg>
    <div class="brand">MERANTE</div>
    <div class="header-icons">
      <svg width="17" height="16" viewBox="0 0 17 16"><path d="M8.5 14.5S1 10 1 5a3.7 3.7 0 0 1 7.5-1A3.7 3.7 0 0 1 16 5c0 5-7.5 9.5-7.5 9.5z" fill="none" stroke="#333" stroke-width="1.2"/></svg>
      <svg width="18" height="16" viewBox="0 0 18 16"><path d="M0 1h3l2 9h10l2-7H4.5M6 5h10M6.5 8h9" fill="none" stroke="#333" stroke-width="1.2"/><circle cx="6.5" cy="13.5" r="1.3" fill="#333"/><circle cx="14" cy="13.5" r="1.3" fill="#333"/></svg>
    </div>
    <div class="search"><span>Finde Dein Lieblingsprodukt...</span>
      <svg width="17" height="17" viewBox="0 0 17 17"><circle cx="7" cy="7" r="5.8" fill="none" stroke="#2b2d6e" stroke-width="1.5"/><path d="M11.2 11.2 16 16" stroke="#2b2d6e" stroke-width="1.5"/></svg>
    </div>
  </header>

  <section class="hero" role="img" aria-label="Dunkles Stimmungsfoto mit Keramikschalen">
    <h1>Produkte</h1>
    <nav class="category-tabs">
      <div class="tab">Geschenke</div>
      <div class="tab is-active">Teller</div>
      <div class="tab">Accessoires</div>
      <div class="tab"></div>
    </nav>
  </section>

  <div class="toolbar">
    <div class="filter">Filter
      <svg width="18" height="17" viewBox="0 0 18 17"><path d="M1 1h16l-6 7v7l-4-2V8z" fill="none" stroke="#2b2d6e" stroke-width="1.2" stroke-linejoin="round"/></svg>
    </div>
    <div class="sort">meistverkauft
      <svg width="14" height="8" viewBox="0 0 14 8"><path d="M1 1l6 6 6-6" fill="none" stroke="#2b2d6e" stroke-width="1.6"/></svg>
    </div>
  </div>

  <main class="product-grid">
    <article class="card">
      <svg class="fav" width="14" height="13" viewBox="0 0 17 16"><path d="M8.5 14.5S1 10 1 5a3.7 3.7 0 0 1 7.5-1A3.7 3.7 0 0 1 16 5c0 5-7.5 9.5-7.5 9.5z" fill="none" stroke="#444" stroke-width="1.3"/></svg>
      <div class="plate" role="img" aria-label="Produktfoto: flacher Teller mit Reaktivglasur"></div>
      <h2>Produktname</h2><p class="desc">Teller 27 cm, flach</p><p class="price">24,95 €</p>
      <div class="cart-btn"><svg width="18" height="16" viewBox="0 0 18 16"><path d="M0 1h3l2 9h10l2-7H4.5M6 5h10M6.5 8h9" fill="none" stroke="#2b2d6e" stroke-width="1.4"/><circle cx="6.5" cy="13.5" r="1.4" fill="#2b2d6e"/><circle cx="14" cy="13.5" r="1.4" fill="#2b2d6e"/></svg></div>
    </article>
    <article class="card">
      <svg class="fav" width="14" height="13" viewBox="0 0 17 16"><path d="M8.5 14.5S1 10 1 5a3.7 3.7 0 0 1 7.5-1A3.7 3.7 0 0 1 16 5c0 5-7.5 9.5-7.5 9.5z" fill="none" stroke="#444" stroke-width="1.3"/></svg>
      <div class="plate" role="img" aria-label="Produktfoto: flacher Teller mit Reaktivglasur"></div>
      <h2>Produktname</h2><p class="desc">Teller 27 cm, flach</p><p class="price">24,95 €</p>
      <div class="cart-btn is-hover"><svg width="18" height="16" viewBox="0 0 18 16"><path d="M0 1h3l2 9h10l2-7H4.5M6 5h10M6.5 8h9" fill="none" stroke="#fff" stroke-width="1.4"/><circle cx="6.5" cy="13.5" r="1.4" fill="#fff"/><circle cx="14" cy="13.5" r="1.4" fill="#fff"/></svg></div>
    </article>
    <article class="card">
      <svg class="fav" width="14" height="13" viewBox="0 0 17 16"><path d="M8.5 14.5S1 10 1 5a3.7 3.7 0 0 1 7.5-1A3.7 3.7 0 0 1 16 5c0 5-7.5 9.5-7.5 9.5z" fill="none" stroke="#444" stroke-width="1.3"/></svg>
      <div class="plate" role="img" aria-label="Produktfoto: flacher Teller mit Reaktivglasur"></div>
      <h2>Produktname</h2><p class="desc">Teller 27 cm, flach</p><p class="price">24,95 €</p>
      <div class="cart-btn"><svg width="18" height="16" viewBox="0 0 18 16"><path d="M0 1h3l2 9h10l2-7H4.5M6 5h10M6.5 8h9" fill="none" stroke="#2b2d6e" stroke-width="1.4"/><circle cx="6.5" cy="13.5" r="1.4" fill="#2b2d6e"/><circle cx="14" cy="13.5" r="1.4" fill="#2b2d6e"/></svg></div>
    </article>
    <article class="card">
      <svg class="fav" width="14" height="13" viewBox="0 0 17 16"><path d="M8.5 14.5S1 10 1 5a3.7 3.7 0 0 1 7.5-1A3.7 3.7 0 0 1 16 5c0 5-7.5 9.5-7.5 9.5z" fill="none" stroke="#444" stroke-width="1.3"/></svg>
      <div class="plate" role="img" aria-label="Produktfoto: flacher Teller mit Reaktivglasur"></div>
      <h2>Produktname</h2><p class="desc">Teller 27 cm, flach</p><p class="price">24,95 €</p>
      <div class="cart-btn"><svg width="18" height="16" viewBox="0 0 18 16"><path d="M0 1h3l2 9h10l2-7H4.5M6 5h10M6.5 8h9" fill="none" stroke="#2b2d6e" stroke-width="1.4"/><circle cx="6.5" cy="13.5" r="1.4" fill="#2b2d6e"/><circle cx="14" cy="13.5" r="1.4" fill="#2b2d6e"/></svg></div>
    </article>
    <article class="card">
      <svg class="fav" width="14" height="13" viewBox="0 0 17 16"><path d="M8.5 14.5S1 10 1 5a3.7 3.7 0 0 1 7.5-1A3.7 3.7 0 0 1 16 5c0 5-7.5 9.5-7.5 9.5z" fill="none" stroke="#444" stroke-width="1.3"/></svg>
      <div class="plate" role="img" aria-label="Produktfoto: flacher Teller mit Reaktivglasur"></div>
      <h2>Produktname</h2><p class="desc">Teller 27 cm, flach</p><p class="price">24,95 €</p>
      <div class="cart-btn"><svg width="18" height="16" viewBox="0 0 18 16"><path d="M0 1h3l2 9h10l2-7H4.5M6 5h10M6.5 8h9" fill="none" stroke="#2b2d6e" stroke-width="1.4"/><circle cx="6.5" cy="13.5" r="1.4" fill="#2b2d6e"/><circle cx="14" cy="13.5" r="1.4" fill="#2b2d6e"/></svg></div>
    </article>
    <article class="card">
      <svg class="fav" width="14" height="13" viewBox="0 0 17 16"><path d="M8.5 14.5S1 10 1 5a3.7 3.7 0 0 1 7.5-1A3.7 3.7 0 0 1 16 5c0 5-7.5 9.5-7.5 9.5z" fill="none" stroke="#444" stroke-width="1.3"/></svg>
      <div class="plate" role="img" aria-label="Produktfoto: flacher Teller mit Reaktivglasur"></div>
      <h2>Produktname</h2><p class="desc">Teller 27 cm, flach</p><p class="price">24,95 €</p>
      <div class="cart-btn"><svg width="18" height="16" viewBox="0 0 18 16"><path d="M0 1h3l2 9h10l2-7H4.5M6 5h10M6.5 8h9" fill="none" stroke="#2b2d6e" stroke-width="1.4"/><circle cx="6.5" cy="13.5" r="1.4" fill="#2b2d6e"/><circle cx="14" cy="13.5" r="1.4" fill="#2b2d6e"/></svg></div>
    </article>
  </main>
</div>
</body>
</html>
```